Speisekarten-Design für Gastronomiebetrieb
Zielgruppe
Wir sind ein Gastronomiebetrieb in einer Studentenstadt. Unsere Hauptzielgruppe sind junge Menschen und Studenten, aber auch älteres Puplikum. Wir möchten gerne ein neues Speisekartendesign, da unser aktuelles seit über 10 Jahren sich kaum verändert hat.
Aufgabenstellung
Gerne könne Sie sich die aktulle Speisekarte auf der unserer Hompeage anschauen: www.lumora-kueche.de
Auf der Frontseite soll die Farbrichtung Orange und natürlich das Logo beibehalten werden. Für die restlichen Seiten gibt es diese Einschränkung nicht. Uns ist wichtig, dass die Speisekarte modern, bunt und peppig ist. Das heisst möglichst mit kräftigen Farben und Bildern von Speisen und Getränken arbeiten.

```html
<!DOCTYPE html>
<html lang="de">
<head>
<meta charset="utf-8">
<title>Lumora – Speisekarte</title>
<link href="https://fonts.googleapis.com/css2?family=Courgette&family=Roboto:wght@400;500;700;900&display=swap" rel="stylesheet">
<style>
  :root{
    --stage:#dcdcdc;
    --orange:#f3a72a;
    --red:#c0282f;
    --brown-dark:#4a1e10;
    --rust:#c8501b;
    --olive:#b58a2a;
    --cream:#f3e0c0;
    --cream-light:#f6e7cf;
    --brown-mid:#5e3418;
    --taupe:#cbb4a2;
    --gold:#f0b43a;
    --gold-text:#c2861f;
    --ink:#3a1a0c;
    --white:#ffffff;
  }
  *{box-sizing:border-box;margin:0;padding:0}
  html,body{width:1200px;height:2676px;overflow:hidden}
  body{background:var(--stage);position:relative;font-family:"Roboto",Arial,sans-serif;color:var(--ink)}
  .abs{position:absolute}
  .script{font-family:"Courgette",cursive}

  /* Cover */
  .cover{left:411px;top:130px;width:384px;height:795px;background:var(--orange)}
  .cover__strip{left:0;top:0;width:69px;height:100%;background:var(--red)}
  .cover__tagline{left:34px;top:168px;transform:translate(-50%,-50%) rotate(-90deg);white-space:nowrap;color:var(--orange);font-size:20px;letter-spacing:1px}
  .cover__name{left:69px;right:24px;top:20px;text-align:right;font-weight:900;font-size:56px;color:var(--red);letter-spacing:2px}
  .cover__sub{right:24px;top:82px;font-weight:700;font-size:14px;letter-spacing:3px;color:var(--brown-dark)}
  .cover__photo{left:174px;width:166px;height:166px;border-radius:50%;border:7px solid #e2c58e}
  .cover__address{left:69px;right:0;top:717px;text-align:center;font-size:12px;line-height:16px;color:var(--brown-dark)}
  .cover__address strong{font-size:14px;letter-spacing:1.5px}

  /* Spreads */
  .spread{left:198px;width:768px;background:var(--white)}
  .col{position:absolute;top:0;width:384px}
  .col--left{left:0}
  .col--right{left:384px}

  .band{position:relative;display:flex;align-items:center;background:var(--brown-dark)}
  .band__tab{width:89px;height:100%;position:relative}
  .band__tab::after{content:"";position:absolute;right:-14px;top:50%;transform:translateY(-50%);border-left:14px solid;border-left-color:inherit;border-top:12px solid transparent;border-bottom:12px solid transparent}
  .band__title{font-family:"Courgette",cursive;color:var(--gold);font-size:27px;padding-left:26px;white-space:nowrap}
  .tab--orange{background:var(--orange);border-color:var(--orange)}
  .tab--rust{background:var(--rust);border-color:var(--rust)}
  .tab--olive{background:var(--olive);border-color:var(--olive)}

  .tile{position:relative;display:flex;height:144px}
  .tile__photo{width:205px;height:100%;flex:none}
  .tile__text{flex:1;position:relative;background:var(--cream);padding:12px 12px 0 12px}
  .tile__text h3{font-family:"Courgette",cursive;font-weight:400;font-size:19px;line-height:23px;color:var(--ink)}
  .tile__text p{font-size:11.5px;line-height:14px;margin-top:8px}
  .tile__price{position:absolute;right:18px;bottom:16px;font-family:"Courgette",cursive;font-size:20px}
  .tile__price sup{font-size:11px}
  .tile__text--left::before,.tile__text--right::after{content:"";position:absolute;top:50%;transform:translateY(-50%);border-top:12px solid transparent;border-bottom:12px solid transparent}
  .tile__text--left::before{left:-12px;border-right:12px solid var(--cream)}
  .tile__text--right::after{right:-12px;border-left:12px solid var(--cream);z-index:2}
  .tile--dark .tile__text{background:var(--brown-mid);color:var(--cream)}
  .tile--dark .tile__text h3{color:var(--cream)}
  .tile--dark .tile__text--left::before{border-right-color:var(--brown-mid)}
  .tile--taupe .tile__text{background:var(--taupe)}
  .tile--taupe .tile__text--left::before{border-right-color:var(--taupe)}
  .tile--taupe .tile__text--right::after{border-left-color:var(--taupe)}

  .menu{list-style:none}
  .menu li{position:relative;font-size:11.5px;line-height:14px}
  .menu .qty{position:absolute;left:0}
  .menu .item{display:block;font-weight:500}
  .menu .desc{display:block;font-size:9.5px;line-height:11.5px;color:var(--gold-text)}
  .menu .price{position:absolute;top:0}
</style>
</head>
<body>

<!-- Cover -->
<section class="cover abs">
  <div class="cover__strip abs"></div>
  <div class="cover__tagline abs script">Café • Bar • Restaurant</div>
  <div class="cover__name abs">LUMORA</div>
  <div class="cover__sub abs">SPEISEKARTE</div>
  <div class="cover__photo abs" style="top:126px;background:radial-gradient(circle at 45% 45%,#e9cf9c,#a8793e 70%,#5a3a1c)" role="img" aria-label="Foto: Korb mit frischen Brötchen"></div>
  <div class="cover__photo abs" style="top:317px;background:radial-gradient(circle at 50% 55%,#c7462a,#6b8a2a 45%,#3b2414 80%)" role="img" aria-label="Foto: Burger mit Tomate und Salat"></div>
  <div class="cover__photo abs" style="top:508px;background:radial-gradient(circle at 50% 65%,#d4553a,#6a3a1e 50%,#1f150f 85%)" role="img" aria-label="Foto: Cocktail mit Minze vor Barbeleuchtung"></div>
  <div class="cover__address abs">
    <strong>Lumora Gießen</strong><br>
    Lindenweg 12<br>
    35390 - Gießen<br>
    Tel.: 0641 - 55019
  </div>
</section>

<!-- Spread 1 -->
<section class="spread abs" style="top:944px;height:796px">
  <div class="abs" style="left:0;top:0;width:768px;height:138px;background:linear-gradient(90deg,#5a3a2a,#b88a55 35%,#e39a2e 60%,#a86a2a 80%,#5a3a20)" role="img" aria-label="Foto: große dekorative Holzbuchstaben vor orangefarbener Wand"></div>

  <div class="col col--left" style="top:138px">
    <div class="band" style="height:82px"><div class="band__tab tab--orange"></div><div class="band__title">Aktionen und Angebote</div></div>
    <div class="tile">
      <div class="tile__photo" style="background:radial-gradient(circle at 50% 55%,#e0621f,#4aa0a8 45%,#6b5a48 75%)" role="img" aria-label="Foto: Tomatensuppe in türkiser Schale"></div>
      <div class="tile__text tile__text--left"><h3>Tomatensuppe</h3><p>Some description. Lorem ipsum dolor sit amet, consecte­tur adipiscing elit.</p><div class="tile__price">€16.<sup>90</sup></div></div>
    </div>
    <div class="tile">
      <div class="tile__text tile__text--right"><h3>Sonntag - Pizzatag</h3><p>Alle Pizzen<br>Lorem ipsum dolor<br>sit amet</p><div class="tile__price" style="right:26px">€5.<sup>90</sup></div></div>
      <div class="tile__photo" style="background:radial-gradient(circle at 50% 50%,#c8642a,#7a3a1c 50%,#2a221e 80%)" role="img" aria-label="Foto: geschnittene Pizza auf dunklem Untergrund"></div>
    </div>
    <div class="tile">
      <div class="tile__photo" style="background:linear-gradient(90deg,#8fb83a,#d83a2a 45%,#9cc04a 75%,#3a1a10)" role="img" aria-label="Foto: bunte Cocktails an der Bar"></div>
      <div class="tile__text tile__text--left"><h3>Täglich -<br>Happy Hour</h3><p>Vivamus volutpat urna adipi­scing elit</p><div class="tile__price">€9.<sup>90</sup></div></div>
    </div>
    <div class="tile">
      <div class="tile__text tile__text--right"><h3>Sonntagsbrunch</h3><p>Some description. Lorem ipsum dolor sit amet, conleo facilisis non etur adipiscing elit</p><div class="tile__price" style="right:26px">nur €7.<sup>90</sup></div></div>
      <div class="tile__photo" style="background:radial-gradient(circle at 50% 60%,#d89060,#e8e0d0 50%,#8a3a4a 75%,#3a2a20)" role="img" aria-label="Foto: Lachsfilet mit Salat und Zwiebeln"></div>
    </div>
  </div>

  <div class="col col--right" style="top:138px">
    <div class="band" style="height:82px"><div class="band__tab tab--rust"></div><div class="band__title">Frühstück</div></div>
    <div class="tile">
      <div class="tile__photo" style="background:radial-gradient(circle at 50% 45%,#e8d0b0,#8a5a2a 35%,#2f6a5e 55%,#7a4a2a 85%)" role="img" aria-label="Foto: Cappuccino mit Latte-Art"></div>
      <div class="tile__text tile__text--left"><h3>Zu jedem Frühstück</h3><p style="margin-top:6px">Mo-Do. 10:00-13:00<br>Fr. &amp; Sa 10:00-15:00<br>gibt es Kaffee und Tee<br>so viel Sie möchten</p></div>
    </div>
    <ul class="menu" style="position:absolute;left:64px;top:257px;width:300px">
      <li style="margin-bottom:26px"><span class="qty">1</span><span style="margin-left:32px" class="item">Kleines Frühstück</span><span style="margin-left:32px" class="desc">1 Vollkornbrötchen • Butter &amp; Marmelade</span><span class="price" style="left:242px">€4.50</span></li>
      <li style="margin-bottom:15px"><span class="qty">2</span><span style="margin-left:32px" class="item">Großes Frühstück</span><span style="margin-left:32px" class="desc">2 Brötchen • Butter &amp; Marmelade • Schinken<br>Käse • Salami • 1 Ei • 1 Milchkaffee</span><span class="price" style="left:242px">€6.90</span></li>
      <li style="margin-bottom:15px"><span class="qty">1</span><span style="margin-left:32px" class="item">Kleines Frühstück</span><span style="margin-left:32px" class="desc">1 Vollkornbrötchen • Butter &amp; Marmelade<br>1 Vollkornbrötchen • Butter &amp; Marmelade<br>Käse • Salami • 1 Ei • 1 Milchkaffee</span><span class="price" style="left:242px">€4.50</span></li>
      <li style="margin-bottom:15px"><span class="qty">2</span><span style="margin-left:32px" class="item">Großes Frühstück</span><span style="margin-left:32px" class="desc">2 Brötchen • Butter &amp; Marmelade • Schinken<br>Käse • Salami • 1 Ei • 1 Milchkaffee</span><span class="price" style="left:242px">€6.90</span></li>
      <li style="margin-bottom:15px"><span class="qty">1</span><span style="margin-left:32px" class="item">Kleines Frühstück</span><span style="margin-left:32px" class="desc">1 Vollkornbrötchen • Butter &amp; Marmelade<br>Käse • Salami • 1 Ei • 1 Milchkaffee</span><span class="price" style="left:242px">€4.50</span></li>
      <li style="margin-bottom:15px"><span class="qty">2</span><span style="margin-left:32px" class="item">Großes Frühstück</span><span style="margin-left:32px" class="desc">2 Brötchen • Butter &amp; Marmelade • Schinken<br>Käse • Salami • 1 Ei • 1 Milchkaffee</span><span class="price" style="left:242px">€6.90</span></li>
      <li><span class="qty">1</span><span style="margin-left:32px" class="item">Kleines Frühstück</span><span style="margin-left:32px" class="desc">1 Vollkornbrötchen • Butter &amp; Marmelade</span><span class="price" style="left:242px">€4.50</span></li>
    </ul>
  </div>
</section>

<!-- Spread 2 -->
<section class="spread abs" style="top:1766px;height:794px">
  <div class="col col--left">
    <div class="band" style="height:70px"><div class="band__tab tab--orange"></div><div class="band__title">Suppen</div></div>
    <div class="tile tile--dark">
      <div class="tile__photo" style="background:radial-gradient(circle at 50% 55%,#e0621f,#4aa0a8 45%,#6b5a48 75%)" role="img" aria-label="Foto: Tomatensuppe in türkiser Schale"></div>
      <div class="tile__text tile__text--left"><h3>Unsere Suppen…</h3><p>… werden mit ofenfrischen Pizzabrötchen serviert.</p></div>
    </div>
    <ul class="menu" style="position:absolute;left:48px;top:231px;width:300px">
      <li style="margin-bottom:13px"><span class="qty">30</span><span class="item" style="margin-left:33px">Tomatensuppen</span><span class="price" style="left:242px">€4.50</span></li>
      <li style="margin-bottom:13px"><span class="qty">30</span><span class="item" style="margin-left:33px">Tomatensuppen</span><span class="price" style="left:242px">€4.50</span></li>
      <li><span class="qty">30</span><span class="item" style="margin-left:33px">Tomatensuppen</span><span class="price" style="left:242px">€4.50</span></li>
    </ul>
    <div class="band" style="position:absolute;top:356px;width:384px;height:69px"><div class="band__tab tab--olive" style="width:80px"></div><div class="band__title">Ofenfrische Baguettes</div></div>
    <div class="tile tile--taupe" style="position:absolute;top:425px;width:384px">
      <div class="tile__photo" style="background:linear-gradient(160deg,#e8c890,#c08a4a 40%,#8a9a5a 60%,#c07a3a)" role="img" aria-label="Foto: überbackenes Baguette mit Kräutern"></div>
      <div class="tile__text tile__text--left"><h3>Unsere Baguettes…</h3><p>… jeweils mit Remoulade, überbacken mit Käse, dazu Salatbeilage.</p></div>
    </div>
    <ul class="menu" style="position:absolute;left:48px;top:601px;width:300px">
      <li style="margin-bottom:13px"><span class="qty">59</span><span class="item" style="margin-left:33px">mit Tomaten</span><span class="price" style="left:242px">€4.50</span></li>
      <li style="margin-bottom:13px"><span class="qty">59</span><span class="item" style="margin-left:33px">mit Thunfisch und Ei</span><span class="price" style="left:242px">€4.50</span></li>
      <li style="margin-bottom:13px"><span class="qty">59</span><span class="item" style="margin-left:33px">mit Tomaten und Mozzarella</span><span class="price" style="left:242px">€4.50</span></li>
      <li style="margin-bottom:13px"><span class="qty" style="top:7px">61</span><span class="item" style="margin-left:33px">mit Tomaten und Hänchenbrust,<br>überbacken mit Mozzarella</span><span class="price" style="left:242px;top:7px">€5.90</span></li>
      <li><span class="qty" style="top:7px">61</span><span class="item" style="margin-left:33px">mit Tomaten und Hänchenbrust,<br>überbacken mit Mozzarella</span><span class="price" style="left:242px;top:7px">€5.90</span></li>
    </ul>
  </div>

  <div class="col col--right" style="height:794px;background:var(--cream-light)">
    <div class="band" style="height:70px"><div class="band__tab tab--rust"></div><div class="band__title">Kleine Speisen</div></div>
    <ul class="menu" style="position:absolute;left:53px;top:82px;width:310px">
      <li style="margin-bottom:16px"><span class="qty">1</span><span class="item" style="margin-left:33px">Kleines Frühstück</span><span class="desc" style="margin-left:33px">1 Vollkornbrötchen • Butter &amp; Marmelade</span><span class="price" style="left:203px">€4.50</span></li>
      <li style="margin-bottom:16px"><span class="qty">2</span><span class="item" style="margin-left:33px">Großes Frühstück</span><span class="desc" style="margin-left:33px">2 Brötchen • Butter &amp; Marmelade • Schinken<br>Käse • Salami • 1 Ei • 1 Milchkaffee</span><span class="price" style="left:203px">€6.90</span></li>
      <li style="margin-bottom:16px"><span class="qty">1</span><span class="item" style="margin-left:33px">Kleines Frühstück</span><span class="desc" style="margin-left:33px">1 Vollkornbrötchen • Butter &amp; Marmelade<br>1 Vollkornbrötchen • Butter &amp; Marmelade<br>Käse • Salami • 1 Ei • 1 Milchkaffee</span><span class="price" style="left:203px">€4.50</span></li>
      <li style="margin-bottom:16px"><span class="qty">2</span><span class="item" style="margin-left:33px">Großes Frühstück</span><span class="desc" style="margin-left:33px">2 Brötchen • Butter &amp; Marmelade • Schinken<br>Käse • Salami • 1 Ei • 1 Milchkaffee</span><span class="price" style="left:203px">€6.90</span></li>
      <li style="margin-bottom:16px"><span class="qty">1</span><span class="item" style="margin-left:33px">Kleines Frühstück</span><span class="desc" style="margin-left:33px">1 Vollkornbrötchen • Butter &amp; Marmelade<br>Käse • Salami • 1 Ei • 1 Milchkaffee</span><span class="price" style="left:203px">€4.50</span></li>
      <li><span class="qty">2</span><span class="item" style="margin-left:33px">Großes Frühstück</span><span class="desc" style="margin-left:33px">2 Brötchen • Butter &amp; Marmelade • Schinken<br>Käse • Salami • 1 Ei • 1 Milchkaffee</span><span class="price" style="left:203px">€6.90</span></li>
    </ul>
    <div class="band" style="position:absolute;top:399px;width:384px;height:67px"><div class="band__tab tab--orange"></div><div class="band__title">Burger</div></div>
    <ul class="menu" style="position:absolute;left:38px;top:478px;width:320px">
      <li style="margin-bottom:16px"><span class="qty">20</span><span class="item" style="margin-left:36px">Lumora Burger</span><span class="desc" style="margin-left:36px">1 Vollkornbrötchen • Butter &amp; Marmelade</span><span class="price" style="left:218px">€8.50</span></li>
      <li style="margin-bottom:16px"><span class="qty">2</span><span class="item" style="margin-left:36px">Großes Frühstück</span><span class="desc" style="margin-left:36px">2 Brötchen • Butter &amp; Marmelade • Schinken<br>Käse • Salami • 1 Ei • 1 Milchkaffee</span><span class="price" style="left:218px">€6.90</span></li>
      <li><span class="qty">1</span><span class="item" style="margin-left:36px">Kleines Frühstück</span><span class="desc" style="margin-left:36px">1 Vollkornbrötchen • Butter &amp; Marmelade<br>1 Vollkornbrötchen • Butter &amp; Marmelade<br>Käse • Salami • 1 Ei • 1 Milchkaffee</span><span class="price" style="left:218px">€4.50</span></li>
    </ul>
    <div class="tile tile--taupe" style="position:absolute;top:650px;width:384px">
      <div class="tile__photo" style="background:radial-gradient(circle at 45% 60%,#b8442a,#6a8a2a 35%,#8a5a2a 55%,#2a2420 85%)" role="img" aria-label="Foto: Burger mit Pommes frites"></div>
      <div class="tile__text tile__text--left"><h3>Unsere Burger…</h3><p>… werden mit 100% Rind­fleisch zubereitet und mit Pommes frites und Salat serviert.</p></div>
    </div>
  </div>
</section>

</body>
</html>
```